Business cards/ stationery design for a transport consultancy
Freight Lantern
Business cards/ stationery design for a transport consultancy - Consulting
Creative Brief
Use standard fonts
Use either logo font (EUROSTILE LT STD) or complimentary font type
Simple
Declan Brolly
Managing Director
Ground Floor 27/ 28 Wexholm Yard Dublin 2 Ireland
dbrolly@freightlantern.com
www.freightlantern.com
Registered office address, and company registration number will need to be included as a footer at bottom of letter template.
Emphasis on designs should be on conveying a professional image.

```html
<!DOCTYPE html>
<html lang="en">
<head>
<meta charset="utf-8">
<title>Freight Lantern — Business Cards</title>
<link rel="stylesheet" href="https://fonts.googleapis.com/css2?family=Michroma&family=Open+Sans:wght@400;600;700&display=swap">
<style>
  :root {
    --bg: #1e1f22;
    --blue-deep: #0b2f63;
    --blue-mid: #1a5fa8;
    --blue-light: #3d86d0;
    --band-white: #f4f6f8;
    --band-grey: #5c5f63;
    --band-grey-dark: #3f4245;
    --ink-blue: #154a8c;
    --text-light: #ffffff;
    --text-soft: #cfdcec;
  }
  * { margin: 0; padding: 0; box-sizing: border-box; }
  html, body { width: 1200px; height: 901px; overflow: hidden; background: var(--bg); }
  .canvas {
    position: relative; width: 1200px; height: 901px;
    display: flex; align-items: center; justify-content: center; gap: 40px;
  }
  .card {
    position: relative; width: 520px; height: 336px; border-radius: 18px; overflow: hidden;
    background: linear-gradient(135deg, var(--blue-light) 0%, var(--blue-mid) 40%, var(--blue-deep) 100%);
    font-family: "Open Sans", Arial, sans-serif; color: var(--text-light);
  }
  .brand { display: flex; align-items: center; gap: 16px; }
  .brand-dot { width: 62px; height: 62px; border-radius: 50%; flex: none; }
  .brand-name {
    font-family: "Michroma", "Eurostile", sans-serif; font-size: 26px; line-height: 1.15;
    letter-spacing: 1px; text-transform: uppercase;
  }

  /* back card */
  .card-back .holder { position: absolute; left: 34px; top: 34px; }
  .holder-name { font-size: 17px; font-weight: 700; }
  .holder-title { font-size: 10px; color: var(--text-soft); margin-top: 2px; }
  .card-back .band {
    position: absolute; left: 0; top: 92px; width: 480px; height: 100px;
    border-radius: 0 50px 50px 0;
    background: linear-gradient(180deg, var(--band-grey) 0%, var(--band-grey-dark) 100%);
    display: flex; align-items: center; padding-left: 34px;
  }
  .card-back .brand-dot { background: var(--text-light); }
  .card-back .brand-name { color: var(--text-light); font-size: 22px; }
  .card-back .details {
    position: absolute; left: 34px; right: 30px; bottom: 34px;
    display: flex; font-size: 12px; line-height: 1.55;
  }
  .address { width: 190px; }
  .contact { border-left: 1px solid rgba(255,255,255,0.5); padding-left: 18px; }
  .contact-row { display: flex; align-items: center; gap: 8px; }
  .contact-row svg { width: 12px; height: 12px; fill: var(--text-light); flex: none; }

  /* front card */
  .card-front .band {
    position: absolute; left: 0; right: 0; top: 118px; height: 112px;
    background: var(--band-white);
    display: flex; align-items: center; padding-left: 40px;
  }
  .card-front .brand-dot { background: var(--ink-blue); width: 70px; height: 70px; }
  .card-front .brand-name { color: var(--ink-blue); }
</style>
</head>
<body>
<main class="canvas">
  <section class="card card-back" aria-label="Business card back">
    <div class="holder">
      <p class="holder-name">Declan Brolly</p>
      <p class="holder-title">Managing Director</p>
    </div>
    <div class="band">
      <div class="brand">
        <span class="brand-dot"></span>
        <span class="brand-name">Freight<br>Lantern</span>
      </div>
    </div>
    <div class="details">
      <p class="address">Ground Floor<br>27/ 28 Wexholm Yard<br>Dublin 2, Ireland</p>
      <div class="contact">
        <p class="contact-row">
          <svg viewBox="0 0 24 24" aria-hidden="true"><path d="M2 5h20v14H2z M2 5l10 8 10-8" fill="none" stroke="#fff" stroke-width="2"/></svg>
          dbrolly@freightlantern.com
        </p>
        <p class="contact-row">
          <svg viewBox="0 0 24 24" aria-hidden="true"><circle cx="12" cy="12" r="10" fill="none" stroke="#fff" stroke-width="2"/><path d="M2 12h20M12 2c4 4 4 16 0 20M12 2c-4 4-4 16 0 20" fill="none" stroke="#fff" stroke-width="2"/></svg>
          www.freightlantern.com
        </p>
      </div>
    </div>
  </section>

  <section class="card card-front" aria-label="Business card front">
    <div class="band">
      <div class="brand">
        <span class="brand-dot"></span>
        <span class="brand-name">Freight<br>Lantern</span>
      </div>
    </div>
  </section>
</main>
</body>
</html>
```